I need to launch a new website that more accurately reflects what we do as a business. We are an IT Reseller that specialises in delivering innovative solutions covering supply, implementation and support. My current website is www.vornetikx.com and was something I designed myself on the Hub Nimbo website. This was fine for the first 2 years but now I need something more professional and detailed. A couple of websites for companies similar to Brindle KTR are www.quarvolen.co.uk and www.ferrimund.co.uk. By looking at these it will hopefully give you an idea as to what I am trying to achieve.

Target Market(s)

UK based companies with between 30-250 employees, no fixed vertical

Coding

Coded - Design and coding required

Number of Pages Required

4 page

Font styles to use
Sans Serif

Colors
33a6d7
0592cd
85cae6

Requirements
Must have
• Contact details page to include a "Get in touch with us " section, About Us page, IT Support page to include the headings 1/ Proactive Monitoring 2/ 24 x 7 Support 3/ Security and Data Back-up 4/ Built-in Compliance (GDPR) 5/ Responsive IT Support. I am happy to provide the wording for these headings.
Clean crisp home screen with a Menu offering the requested drop down options.
Nice to have
• Easy to navigate site with a good flow. I have updated a page regarding cloud services, this would be great to have as a separate drop down menu option. I would like to have different Cloud logo's in ideally the Brindle Blue colour. Can you please add the photograph of Thornwick Lodge which is my office in the contact us page.
Should not have
• I definitely DO NOT want a photo/view of London on the home page!!

```html
<!DOCTYPE html>
<html lang="en">
<head>
<meta charset="utf-8">
<title>Brindle KTR — IT Reseller</title>
<link href="https://fonts.googleapis.com/css2?family=Exo+2:wght@400;500;600&family=Ubuntu:ital,wght@0,400;0,500;0,700;1,400&display=swap" rel="stylesheet">
<style>
:root{
  --blue:#1a7fc5;
  --blue-mid:#2691d2;
  --blue-bright:#33a6d7;
  --blue-deep:#0f6fb3;
  --sky:#85cae6;
  --pale:#e4f3fb;
  --ink:#1c1c1c;
  --text:#3a3a3a;
  --white:#ffffff;
  --line:#8a8f94;
}
*{margin:0;padding:0;box-sizing:border-box}
html,body{width:1200px;height:4380px;overflow:hidden}
body{position:relative;font-family:"Ubuntu",sans-serif;color:var(--text);background:var(--white)}
.abs{position:absolute}
h1,h2,h3,.heading{font-family:"Exo 2",sans-serif;font-weight:500}

/* top bar */
.topbar{left:0;top:0;width:1200px;height:38px;background:var(--blue-mid);color:var(--white);font-size:14px}
.topbar .phone{left:110px;top:11px;display:flex;align-items:center;gap:6px}
.topbar .social{right:118px;top:13px;display:flex;gap:12px}
.topbar .social span{width:11px;height:11px;border-radius:50%;background:var(--white);opacity:.9}

/* header */
.header{left:0;top:38px;width:1200px;height:91px;background:var(--white)}
.brand{left:110px;top:24px;display:flex;align-items:center;gap:14px;font-family:"Ubuntu",sans-serif;font-weight:500;font-size:19px;color:var(--ink)}
.brand .mark{width:40px;height:40px;border-radius:50%;background:var(--blue-deep)}
.nav{top:38px;font-size:16px;color:var(--ink);font-weight:500}
.nav.active{color:var(--blue)}
.search{left:1070px;top:39px}

/* hero */
.hero{left:0;top:129px;width:1200px;height:602px;background:linear-gradient(180deg,#2a8fd3 0%,#1d82c8 55%,#1877bd 100%);overflow:hidden}
.hero .glow{left:0;top:340px;width:1200px;height:262px;background:linear-gradient(180deg,rgba(255,255,255,0) 0%,rgba(20,90,150,.35) 100%)}
.hero h1{left:107px;top:144px;width:560px;font-size:36px;line-height:54px;color:var(--white);font-weight:500}
.btn{display:flex;align-items:center;justify-content:center;font-family:"Ubuntu",sans-serif;font-weight:700;font-size:16px;letter-spacing:.2px}
.hero .btn{left:107px;top:393px;width:165px;height:53px;background:var(--white);color:var(--blue)}
.hero .photo{left:662px;top:36px;width:530px;height:530px;border-radius:50%;background:radial-gradient(circle at 55% 40%,#6b5a4e 0%,#2f3a4a 45%,#18243a 100%)}
.dots{left:893px;top:522px;display:flex;gap:5px}
.dots span{width:9px;height:9px;border-radius:50%;background:var(--white)}
.dots span.on{background:var(--blue-bright)}

/* section heads */
.sec-title{width:1200px;left:0;text-align:center;font-family:"Exo 2",sans-serif;font-weight:500;font-size:34px;color:var(--ink)}
.sec-title em{font-style:normal;color:var(--blue)}
.sec-sub{width:1200px;left:0;text-align:center;font-size:16px;line-height:30px;color:var(--text)}

/* services */
.service{width:300px;text-align:center}
.service .icon{width:104px;height:104px;margin:0 auto;border-radius:50%;background:linear-gradient(160deg,var(--blue-bright),var(--blue-deep));display:flex;align-items:center;justify-content:center}
.service h3{margin-top:18px;font-family:"Ubuntu",sans-serif;font-weight:500;font-size:16px;color:var(--ink);letter-spacing:.2px}
.service p{margin-top:10px;font-size:14.5px;line-height:30px;color:var(--text)}

/* about */
.about{left:0;top:1584px;width:1200px;height:558px;background:var(--pale)}
.about .pic{left:95px;top:65px;width:442px;height:442px;border-radius:50%;border:4px solid var(--blue-bright);background:linear-gradient(180deg,#7fb4e0 0%,#c98d5e 50%,#4f6f8a 100%)}
.about h2{left:617px;top:90px;font-size:34px;color:var(--ink)}
.about h2 em{font-style:normal;color:var(--blue)}
.about p{left:617px;top:145px;width:490px;font-size:14.5px;line-height:30px}
.about .btn{left:617px;top:410px;width:165px;height:54px;background:var(--blue);color:var(--white)}

/* testimonials */
.people{left:0;top:2142px;width:1200px;height:569px;background:var(--blue);overflow:hidden}
.people .sec-title,.people .sec-sub{color:var(--white)}
.quote{width:355px;height:243px;background:var(--white);padding:18px 22px}
.quote.faded{opacity:.55}
.quote .mk{font-family:"Exo 2",sans-serif;font-size:26px;line-height:18px;color:var(--blue);font-style:italic}
.quote p{margin-top:8px;font-style:italic;font-size:14px;line-height:30px;color:var(--text)}
.quote .who{margin-top:14px;display:flex;align-items:center;gap:18px;font-weight:500;font-size:16px;color:var(--blue);letter-spacing:.5px}
.quote .avatar{width:54px;height:54px;border-radius:50%;background:linear-gradient(160deg,#9aa3ad,#3c4652)}
.arrow{left:84px}

/* blog */
.post{width:316px}
.post .pic{width:316px;height:236px}
.post .date{margin:18px 0 0 9px;font-size:13px;color:var(--blue)}
.post h3{margin:8px 0 0 9px;font-family:"Ubuntu",sans-serif;font-weight:500;font-size:21px;line-height:30px;color:var(--ink)}
.post p{margin:8px 0 0 9px;font-size:14.5px;line-height:30px}
.post .more{margin:0 0 0 9px;font-size:13px;font-weight:500;color:var(--blue)}

/* contact */
.contact{left:0;top:3446px;width:1200px;height:830px;background:var(--pale);overflow:hidden}
.form{left:168px;top:170px;width:849px;height:430px;background:var(--white);border:1px solid #d3e3ee}
.field{border:1px solid var(--line);border-radius:2px;font-size:13px;color:#6a6f74;padding:0 14px;display:flex;align-items:center;background:var(--white)}
.field.msg{align-items:flex-start;padding-top:20px}
.contact .btn{left:512px;top:500px;width:166px;height:54px;background:var(--blue);color:var(--white)}
.skyline{left:40px;top:600px;width:1120px;height:230px;background:linear-gradient(180deg,rgba(133,202,230,0) 0%,rgba(120,180,225,.45) 60%,rgba(80,150,210,.6) 100%)}

.footer{left:0;top:4276px;width:1200px;height:104px;background:var(--blue);color:var(--white);font-size:16px;text-align:center;padding-top:38px}
</style>
</head>
<body>

<!-- top bar -->
<div class="abs topbar">
  <div class="abs phone">
    <svg width="13" height="13" viewBox="0 0 24 24" fill="#fff"><path d="M6.6 10.8a15 15 0 0 0 6.6 6.6l2.2-2.2c.3-.3.7-.4 1-.2 1.1.4 2.3.6 3.6.6.6 0 1 .4 1 1V20c0 .6-.4 1-1 1A17 17 0 0 1 3 4c0-.6.4-1 1-1h3.5c.6 0 1 .4 1 1 0 1.3.2 2.5.6 3.6.1.3 0 .7-.2 1z"/></svg>
    + 1 555 0142 773
  </div>
  <div class="abs social"><span></span><span></span><span></span><span></span></div>
</div>

<!-- header -->
<header class="abs header">
  <div class="abs brand"><span class="mark"></span>Brindle KTR</div>
  <nav>
    <span class="abs nav active" style="left:512px">Home</span>
    <span class="abs nav" style="left:600px">About Us</span>
    <span class="abs nav" style="left:712px">IT Support <svg width="10" height="8" viewBox="0 0 10 8"><path d="M1 2h8L5 7z" fill="#1c1c1c"/></svg></span>
    <span class="abs nav" style="left:850px">Blog</span>
    <span class="abs nav" style="left:925px">Contact Us</span>
  </nav>
  <svg class="abs search" width="16" height="16" viewBox="0 0 16 16" fill="none" stroke="#1c1c1c" stroke-width="2"><circle cx="6.5" cy="6.5" r="5"/><path d="M10.5 10.5 15 15"/></svg>
</header>

<!-- hero -->
<section class="abs hero">
  <div class="abs glow"></div>
  <h1 class="abs">IT Reseller that specialises in deliveringinnovative solutions covering supply,implementation and support.</h1>
  <a class="abs btn">GET STARTED</a>
  <div class="abs photo" role="img" aria-label="Photo of a smiling IT support specialist on the phone at a desk with code screens"></div>
  <div class="abs dots"><span></span><span class="on"></span><span></span><span></span><span></span></div>
</section>

<!-- services -->
<h2 class="abs sec-title" style="top:812px">IT Support <em>Services</em></h2>
<p class="abs sec-sub" style="top:869px">Sed ut perspiciatis unde omnis iste natus error sit voluptatem accusantium doloremque laudantium,<br>totam rem aperiam, eaque ipsa quae ab illo inventore veritatis</p>

<div class="abs service" style="left:122px;top:978px">
  <div class="icon"><svg width="56" height="56" viewBox="0 0 56 56" fill="none" stroke="#fff" stroke-width="2"><rect x="8" y="10" width="30" height="24" rx="2"/><path d="M13 28l7-7 5 4 8-9"/><circle cx="36" cy="34" r="8"/><path d="M42 40l7 7"/></svg></div>
  <h3>PROACTIVE MONITORING</h3>
  <p>Sed ut perspiciatis unde omnis iste natus error sit voluptatem accusantium doloremque laudantium.</p>
</div>
<div class="abs service" style="left:450px;top:978px">
  <div class="icon"><svg width="56" height="56" viewBox="0 0 56 56" fill="none" stroke="#fff" stroke-width="2"><path d="M14 28v-4a14 14 0 0 1 28 0v4"/><rect x="10" y="26" width="7" height="11" rx="2"/><rect x="39" y="26" width="7" height="11" rx="2"/><path d="M42 37c0 6-6 8-12 8"/><path d="M14 50c2-6 8-8 14-8s12 2 14 8"/></svg></div>
  <h3>24 X 7 SUPPORT</h3>
  <p>Sed ut perspiciatis unde omnis iste natus error sit voluptatem accusantium doloremque laudantium.</p>
</div>
<div class="abs service" style="left:776px;top:978px">
  <div class="icon"><svg width="56" height="56" viewBox="0 0 56 56" fill="none" stroke="#fff" stroke-width="2"><path d="M16 24v-6a9 9 0 0 1 18 0v6"/><rect x="11" y="24" width="28" height="24" rx="3"/><circle cx="25" cy="34" r="3"/><path d="M25 37v5"/><path d="M40 30l8 3v6c0 5-4 8-8 9-4-1-8-4-8-9v-6z"/><path d="M37 39l2 2 4-4"/></svg></div>
  <h3>SECURITY AND DATA BACK-UP</h3>
  <p>Sed ut perspiciatis unde omnis iste natus error sit voluptatem accusantium doloremque laudantium.</p>
</div>
<div class="abs service" style="left:285px;top:1254px">
  <div class="icon"><svg width="56" height="56" viewBox="0 0 56 56" fill="none" stroke="#fff" stroke-width="2"><path d="M28 6l18 7v12c0 12-8 20-18 24-10-4-18-12-18-24V13z"/><path d="M28 12l12 5v8c0 8-5 14-12 17-7-3-12-9-12-17v-8z"/><path d="M18 27h20"/></svg></div>
  <h3>BUILT-IN COMPLIANCE (GDPR)</h3>
  <p>Sed ut perspiciatis unde omnis iste natus error sit voluptatem accusantium doloremque laudantium.</p>
</div>
<div class="abs service" style="left:612px;top:1254px">
  <div class="icon"><svg width="56" height="56" viewBox="0 0 56 56" fill="none" stroke="#fff" stroke-width="2"><rect x="8" y="12" width="40" height="28" rx="2"/><path d="M22 48h12M28 40v8"/><rect x="17" y="8" width="22" height="24" rx="2"/><path d="M22 20h12M22 25h8"/></svg></div>
  <h3>RESPONSIVE IT SUPPORT</h3>
  <p>Sed ut perspiciatis unde omnis iste natus error sit voluptatem accusantium doloremque laudantium.</p>
</div>

<!-- about -->
<section class="abs about">
  <div class="abs pic" role="img" aria-label="Photo of a historic bridge over a river in the city with the company name overlaid"></div>
  <h2 class="abs">About <em>Brindle KTR</em></h2>
  <p class="abs">Sed ut perspiciatis unde omnis iste natus error sit voluptatem accus antium doloremque laudantium, totam rem aperiam, eaque ipsa quae ab illo inventore veritatis et quasi architecto beatae vitae dicta sunt explicabo. Nemo enim ipsam voluptatem quia voluptas sit aspernatur aut odit aut fugit, sed quia consequuntur magni dolores eos qui ratione voluptatem sequi nesciunt. Neque porro quisquam est, qui dolorem ipsum quia dolor sit amet, consectetur, adipisci velit, sed quia non numquam eius modi tempora.</p>
  <a class="abs btn">GET STARTED</a>
</section>

<!-- testimonials -->
<section class="abs people">
  <h2 class="abs sec-title" style="top:88px">What Our People Says</h2>
  <p class="abs sec-sub" style="top:145px">Sed ut perspiciatis unde omnis iste natus error sit voluptatem accusantium doloremque laudantium,<br>totam rem aperiam, eaque ipsa quae ab illo inventore veritatis</p>
  <svg class="abs arrow" style="top:326px" width="44" height="14" viewBox="0 0 44 14" fill="none" stroke="#fff" stroke-width="2"><path d="M0 7h42M36 1l6 6-6 6"/></svg>
  <svg class="abs arrow" style="top:367px" width="44" height="14" viewBox="0 0 44 14" fill="none" stroke="#fff" stroke-width="2"><path d="M44 7H2M8 1 2 7l6 6"/></svg>

  <div class="abs quote" style="left:192px;top:233px">
    <div class="mk">“</div>
    <p>Sed ut perspiciatis unde omnis iste natus err or sit voluptatem accusantium doloremque laudantium, totam rem aperiam, eaque ipsa quae ab illo inventore .</p>
    <div class="who"><span class="avatar" role="img" aria-label="Client portrait"></span>MARA QUILL</div>
  </div>
  <div class="abs quote" style="left:578px;top:233px">
    <div class="mk">“</div>
    <p>Sed ut perspiciatis unde omnis iste natus err or sit voluptatem accusantium doloremque laudantium, totam rem aperiam, eaque ipsa quae ab illo inventore .</p>
    <div class="who"><span class="avatar" role="img" aria-label="Client portrait"></span>MARA QUILL</div>
  </div>
  <div class="abs quote faded" style="left:964px;top:233px">
    <div class="mk">“</div>
    <p style="white-space:nowrap">Sed ut perspiciatis unde omnis iste<br>or sit voluptatem accusantium dolo<br>laudantium, totam rem aperiam, ea<br>quae ab illo inventore .</p>
    <div class="who"><span class="avatar" role="img" aria-label="Client portrait"></span>MARA QUILL</div>
  </div>
</section>

<!-- blog -->
<h2 class="abs sec-title" style="top:2793px">Our Latest <em>Blog</em></h2>
<p class="abs sec-sub" style="top:2849px">Sed ut perspiciatis unde omnis iste natus error sit voluptatem accusantium doloremque laudantium,<br>totam rem aperiam, eaque ipsa quae ab illo inventore veritatis</p>

<article class="abs post" style="left:107px;top:2936px">
  <div class="pic" role="img" aria-label="Photo of a team working in a dark network operations room" style="background:linear-gradient(160deg,#3d6f9c,#14273f)"></div>
  <div class="date">18 Dec 2020</div>
  <h3>Sed ut perspiciatis unde omn is iste natus error sit vo.</h3>
  <p>Sed ut perspiciatis unde omnis iste natus error sit voluptatem accusantium</p>
  <div class="more">Read More</div>
</article>
<article class="abs post" style="left:440px;top:2936px">
  <div class="pic" role="img" aria-label="Photo of colleagues smiling together at a computer in an office" style="background:linear-gradient(160deg,#a47a5c,#3b3330)"></div>
  <div class="date">18 Dec 2020</div>
  <h3>Sed ut perspiciatis unde omn is iste natus error sit vo.</h3>
  <p>Sed ut perspiciatis unde omnis iste natus error sit voluptatem accusantium</p>
  <div class="more">Read More</div>
</article>
<article class="abs post" style="left:774px;top:2936px">
  <div class="pic" role="img" aria-label="Photo of a support desk team wearing headsets at their computers" style="background:linear-gradient(160deg,#dfe5ea,#7d8792)"></div>
  <div class="date">18 Dec 2020</div>
  <h3>Sed ut perspiciatis unde omn is iste natus error sit vo.</h3>
  <p>Sed ut perspiciatis unde omnis iste natus error sit voluptatem accusantium</p>
  <div class="more">Read More</div>
</article>

<!-- contact -->
<section class="abs contact">
  <h2 class="abs sec-title" style="top:85px">Get in <em>Touch</em></h2>
  <div class="abs skyline" role="img" aria-label="Line illustration of a city skyline with landmarks"></div>
  <form class="abs form">
    <div class="abs field" style="left:100px;top:43px;width:327px;height:59px">First Name</div>
    <div class="abs field" style="left:435px;top:43px;width:327px;height:59px">Last Name</div>
    <div class="abs field" style="left:100px;top:114px;width:327px;height:59px">Email address</div>
    <div class="abs field" style="left:435px;top:114px;width:327px;height:59px">Phone Number</div>
    <div class="abs field msg" style="left:100px;top:188px;width:662px;height:100px">Message</div>
  </form>
  <a class="abs btn">SUMBIT</a>
</section>

<footer class="abs footer">© Copyrights 2020 Brindle &nbsp;&nbsp;|&nbsp;&nbsp; All Rights Reserved</footer>

</body>
</html>
```